Create New Bussiness Card For New Shoes Store

Vandrule is a store that sells a variety of skateboard shoes such as Kestro, Mollen etc. we also sell some skateboard and all skateboard accessories.
we like black and white style logo, but also like blue as well.
We are fully assembled with a deck, truck, wheels, and bearings. Add some personality to your board with a fun, graphic skateboard deck. Constructed of thick 7 ply maple,
Target Market(s)
Target audience: 12-40 year old
especially for young man
Industry/Entity Type
Industrial
Contact Information for Business Card
Name: Vandrule
Address1: 2483 Harlow Brisket Rd
City: Quenmoor
State: Ohio
Zip: 40912
Country: US
Phone: 614830296
email: markolvenby@plimmail.test

```html
<!DOCTYPE html>
<html lang="en">
<head>
<meta charset="utf-8">
<title>Vandrule Business Card</title>
<link rel="stylesheet" href="https://fonts.googleapis.com/css2?family=Lato:wght@400;700&display=swap">
<style>
  :root {
    --backdrop: #4a3020;
    --card: #a24fa8;
    --ink: #f7eef8;
    --rule: rgba(247, 238, 248, 0.75);
  }
  * { margin: 0; padding: 0; box-sizing: border-box; }
  html, body {
    width: 1137px;
    height: 1200px;
    overflow: hidden;
  }
  body {
    background: var(--backdrop);
    font-family: "Lato", sans-serif;
    position: relative;
  }
  .business-card {
    position: absolute;
    left: 68px;
    top: 314px;
    width: 1000px;
    height: 571px;
    background: var(--card);
    border-radius: 20px;
    color: var(--ink);
  }
  .brand {
    position: absolute;
    left: 0;
    right: 0;
    top: 124px;
    display: flex;
    align-items: center;
    justify-content: center;
    gap: 16px;
  }
  .brand-dot {
    width: 30px;
    height: 30px;
    border: 3px solid var(--ink);
    border-radius: 50%;
  }
  .brand-name {
    font-size: 58px;
    font-weight: 400;
    letter-spacing: 1px;
    line-height: 1;
  }
  .identity {
    position: absolute;
    left: 0;
    right: 0;
    top: 420px;
    display: flex;
    align-items: center;
    justify-content: center;
    gap: 18px;
  }
  .identity-name {
    font-size: 40px;
    font-weight: 700;
    letter-spacing: 1.5px;
  }
  .identity-divider {
    width: 2px;
    height: 34px;
    background: var(--ink);
  }
  .identity-role {
    font-size: 30px;
    font-weight: 400;
    letter-spacing: 1px;
  }
  .rule {
    position: absolute;
    left: 151px;
    width: 698px;
    top: 479px;
    height: 1.5px;
    background: var(--rule);
  }
  .contact {
    position: absolute;
    left: 0;
    right: 0;
    top: 491px;
    text-align: center;
    font-size: 23px;
    letter-spacing: 0.3px;
    white-space: nowrap;
  }
</style>
</head>
<body>
  <div class="business-card">
    <div class="brand">
      <span class="brand-dot"></span>
      <span class="brand-name">Vandrule</span>
    </div>
    <div class="identity">
      <span class="identity-name">Vandrule</span>
      <span class="identity-divider"></span>
      <span class="identity-role">President</span>
    </div>
    <div class="rule"></div>
    <p class="contact">P: 614830296 A: 2483 Harlow Brisket Rd, Quenmoor, QV 40912, USA</p>
  </div>
</body>
</html>
```